Website with a rustic Patriotic Feel

I am looking to design the
Home page I have a mock-up that has the essentials on it like our video, a small slideshow, our plans, and a coverage map, and a small sign up box to be sent a free SIM card.

Eligibility Page: Cool Background with a fill in box that lets the user know if their number is GSM or unlocked.

View Plans page: will have our plans hopefully in their colors with a cool background a walkthrough on Activation.

Activation: If you order your plan first then we send the SIM Card Basically another fill out sheet first name last name ICCID IMEI phone number email

, Contact Us: This is our Customer support page.

Steady Beacon ( this will be our About us page and will have a calendar of Community Volunteer Opportunities.. Right now I have a hodgepodge of different themes that I am going with for the web design. I would like it cohesive with the theme so all of it can fit together nicely.

At the Site map at the bottom we are looking for the basic Menu redirects. quick links to our T&Cs Customer Support and Follow US Buttons as well as a sign up for our Newsletter fill in.

Feel free to redo any of the ads. We are an MVNO like (Brightwave Mobile) we provide network Voice and Data Plans our target audience is first Responders and Military. If you are wondering what that green map is its a coverage map to see where to best have coverage. Right now I have a website that uses CMS and HTML. If you are interested in doing a full redesign of our website we would love it.

Right now our website is www.kelvoro-netlink.example if you need any additional information.

Target Market(s)

First Responders and Military

Coding

Coded - Design and coding required

Number of Pages Required

5+ page

Font styles to use
Sans Serif

Colors
0455a3
0493ce
f0474d
ffffff

Requirements
Must have
• Cohesive and have a powerpoint and coverage map
Should not have
• Anything flowery or kiddish

```html
<!DOCTYPE html>
<html lang="en">
<head>
<meta charset="utf-8">
<title>Eligibility – Kelvoro Netlink Mobile Services</title>
<link href="https://fonts.googleapis.com/css2?family=Barlow:wght@400;500;600;700&display=swap" rel="stylesheet">
<style>
:root{
  --navy:#1b2550;
  --indigo:#2b3990;
  --sky:#b3e0fb;
  --red:#f2322f;
  --green:#2aa632;
  --btn-green:#1e9a27;
  --paper:#e9e9e9;
  --footer:#9b9b9b;
  --footer-dark:#929292;
  --white:#ffffff;
  --ink:#444;
}
*{box-sizing:border-box;margin:0;padding:0}
html,body{width:1000px;height:1200px;overflow:hidden}
body{position:relative;font-family:'Barlow',sans-serif;background:var(--paper);color:var(--ink)}
.abs{position:absolute}
.header{left:0;top:0;width:1000px;height:62px;background:var(--navy)}
.brand{left:186px;top:10px;color:var(--white);font-weight:700;font-size:17px;line-height:1;display:flex;align-items:center;gap:6px}
.brand-dot{width:20px;height:20px;border-radius:50%;background:#2f8fe0}
.brand small{display:block;font-size:9px;letter-spacing:2px;color:var(--red);margin-top:4px}
.nav{top:26px;font-size:8.5px;font-weight:600;color:var(--white);letter-spacing:.3px}
.account{left:750px;top:21px;width:68px;height:22px;background:var(--red);color:var(--white);font-size:8.5px;font-weight:600;display:flex;align-items:center;justify-content:center}
.hero{left:0;top:62px;width:1000px;height:80px;background:var(--sky);text-align:center}
.hero h1{margin-top:25px;font-size:22px;font-weight:700;color:var(--navy)}
.crumbs{font-size:5.5px;color:var(--navy);margin-top:3px}
.crumbs u{margin-right:1px}
.section-title{font-size:15.5px;font-weight:700;color:var(--navy)}
.check-card{left:172px;top:198px;width:677px;height:191px;background:var(--white)}
.photo{background:linear-gradient(160deg,#f4f4f4,#d9d9d9 60%,#e9dccc)}
.field{background:var(--white);border:1px solid #dedede;font-size:6.5px;color:#777;display:flex;align-items:center;padding-left:11px}
.btn-red{background:var(--red);color:var(--white);font-weight:600;display:flex;align-items:center;justify-content:center}
.result{left:426px;top:282px;width:357px;height:81px;background:#edfde9;border:1px solid #7fd57c;text-align:center}
.result p{font-size:7px;color:#666;font-weight:500;margin-top:14px}
.result strong{display:block;font-size:18px;line-height:17px;color:var(--green);font-weight:700;margin-top:3px}
.promo-title{font-weight:700;line-height:1;text-align:center}
.btn-green{background:var(--btn-green);color:var(--white);font-size:8px;font-weight:700;display:flex;align-items:center;justify-content:center}
.faq-open{left:172px;top:622px;width:448px;height:26px;background:#a9a9a9;color:var(--white);font-size:8.5px;font-weight:600;display:flex;align-items:center;justify-content:space-between;padding:0 18px 0 13px}
.faq-body{left:172px;top:648px;width:448px;height:71px;background:var(--white);font-size:6.3px;line-height:11.5px;color:#555;padding:13px 18px 0 19px}
.faq-row{left:172px;width:448px;height:27px;border-bottom:1px solid #c4c8e4;font-size:8.5px;font-weight:600;color:#3a3a3a;display:flex;align-items:center;justify-content:space-between;padding:0 18px 0 13px}
.sim-card{left:640px;top:593px;width:208px;height:182px;background:var(--white);text-align:center}
.sim-card p{font-size:8.5px;color:#333;margin-top:33px}
.sim-card h3{font-size:13px;line-height:14px;color:var(--red);font-weight:500;margin-top:3px}
.footer{left:0;top:974px;width:1000px;height:191px;background:var(--footer)}
.copyright{left:0;top:1165px;width:1000px;height:35px;background:var(--footer-dark);color:var(--white);font-size:5.5px;display:flex;align-items:center;justify-content:center}
.locate{left:198px;top:917px;width:622px;height:96px;background:var(--white)}
.locate h2{position:absolute;left:44px;top:36px;font-size:21px;font-weight:600;color:var(--indigo)}
.col{top:1032px;color:var(--white)}
.col h4{font-size:9px;font-weight:600;margin-bottom:6px}
.col li{list-style:none;font-size:6.7px;line-height:16.7px}
.social{display:flex;gap:9px;margin-top:4px}
.social span{width:12px;height:12px;border-radius:50%;background:var(--white)}
</style>
</head>
<body>
<header class="abs header">
  <div class="abs brand"><span class="brand-dot"></span><div>KELVORO NETLINK<small>MOBILE SERVICES</small></div></div>
  <span class="abs nav" style="left:352px">HOME</span>
  <span class="abs nav" style="left:409px">VIEW PLANS</span>
  <span class="abs nav" style="left:484px">ACTIVATE TODAY</span>
  <span class="abs nav" style="left:578px">CONTACT US</span>
  <span class="abs nav" style="left:653px">STEADY BEACON</span>
  <span class="abs account">MY ACCOUNT</span>
</header>

<section class="abs hero">
  <h1>ELIGIBILITY</h1>
  <div class="crumbs"><u>HOME</u>/ ELIGIBILITY</div>
</section>

<h2 class="abs section-title" style="left:173px;top:161px">CHECK YOUR MOBILE NO IS GSM OR UNLOCKED</h2>

<div class="abs check-card"></div>
<div class="abs photo" role="img" aria-label="Hands holding a smartphone over an open laptop with a small potted plant" style="left:183px;top:225px;width:222px;height:164px"></div>
<div class="abs field" style="left:426px;top:234px;width:237px;height:32px">Mobile no :&nbsp; +1 555 014 7788</div>
<div class="abs btn-red" style="left:663px;top:234px;width:120px;height:32px;font-size:11px">SUBMIT</div>
<div class="abs result">
  <p>Your Mobile no :</p>
  <strong>+1 555 014 7788<br>is unclocked</strong>
</div>
<svg class="abs" style="left:451px;top:308px" width="27" height="27" viewBox="0 0 27 27"><circle cx="13.5" cy="13.5" r="11.5" fill="none" stroke="#2aa632" stroke-width="2.2"/><path d="M8 14l4 4 7-8" fill="none" stroke="#2aa632" stroke-width="2.4" stroke-linecap="round" stroke-linejoin="round"/></svg>

<div class="abs" style="left:171px;top:417px;width:334px;height:141px;background:var(--sky)"></div>
<div class="abs" role="img" aria-label="Police officer, paramedic and firefighter standing together" style="left:183px;top:437px;width:155px;height:121px;background:linear-gradient(90deg,#8fa3c0,#3a4250 50%,#c9d86a)"></div>
<div class="abs promo-title" style="left:325px;top:456px;width:160px;font-size:19px;color:var(--navy)">FIRST RESPONDER<br>DISCOUNT</div>
<div class="abs btn-green" style="left:342px;top:500px;width:142px;height:24px">CLICK HERE FOR DISCOUNT CODE</div>

<div class="abs" role="img" aria-label="Soldier in camouflage uniform talking on a phone over a camouflage pattern" style="left:514px;top:417px;width:334px;height:141px;background:linear-gradient(100deg,#b9ae94 0%,#8a7f66 40%,#4b5a2c 60%,#2c3119 100%)"></div>
<div class="abs promo-title" style="left:680px;top:464px;width:150px;font-size:15.5px;color:var(--white)">MILITARY DISCOUNT</div>
<div class="abs btn-green" style="left:683px;top:486px;width:143px;height:24px">CLICK HERE FOR DISCOUNT CODE</div>

<h2 class="abs section-title" style="left:172px;top:587px;color:var(--indigo)">FREQUENTLY ASKED QUESTIONS</h2>
<div class="abs faq-open"><span>Lorem ipsum dolor sit amet, consectetur adipiscing elit.</span><span>-</span></div>
<div class="abs faq-body">Lorem ipsum dolor sit amet, consectetur adipiscing elit. Sed nec vehicula urna. Proin pulvinar laoreet tellus sed viverra. Morbi non tempor nulla, id varius lorem. Donec a diam tristique turpis sagittis vulputate sed molestie ante. Vivamus porttitor ornare erat, eget finibus dolor feugiat id. Pellentesque elementum urna ac magna venenatis, vel cursus ligula dignissim.</div>
<div class="abs faq-row" style="top:721px"><span>In tincidunt erat quis aliquet rutrum.</span><span>+</span></div>
<div class="abs faq-row" style="top:748px"><span>Maecenas ultricies turpis quis lorem fringilla imperdiet.</span><span>+</span></div>
<div class="abs faq-row" style="top:775px"><span>Nullam at lorem et risus sodales ullamcorper.</span><span>+</span></div>
<div class="abs faq-row" style="top:802px;border-bottom:none"><span>Mauris et diam nec est luctus aliquam suscipit et mi.</span><span>+</span></div>

<aside class="abs sim-card">
  <p>Is your smartphone ready for</p>
  <h3>KELVORO NETLINK<br>connection?</h3>
</aside>
<div class="abs field" style="left:679px;top:677px;width:138px;height:33px">Enter your email</div>
<div class="abs btn-red" style="left:679px;top:715px;width:136px;height:32px;font-size:11px">GET SIM CARD NOW</div>

<footer class="abs footer"></footer>
<div class="abs locate"><h2>SEARCH FOR A LOCATION</h2></div>
<div class="abs field" style="left:505px;top:949px;width:173px;height:33px">Enter your mobile no</div>
<div class="abs btn-red" style="left:678px;top:949px;width:88px;height:33px;font-size:11px">SEARCH NOW</div>

<div class="abs col" style="left:199px"><h4>QUICK LINKS</h4><ul><li>Home</li><li>Catalog</li><li>View Plans</li><li>Activate Today</li><li>Contact Us</li><li>Steady Beacon</li></ul></div>
<div class="abs col" style="left:373px"><h4>DISCLAIMERS</h4><ul><li>Terms &amp; Conditions</li><li>Activating Your Service</li><li>Acceptable Use Policy</li><li>Wireless Privacy Policy</li><li>Coverage Map</li></ul></div>
<div class="abs col" style="left:545px"><h4>CUSTOMER SUPPORT</h4><ul><li>View Plans</li><li>Contact Us</li><li>Phone: +1 (555) 014-2200</li></ul></div>
<div class="abs col" style="left:714px"><h4>FOLLOW US</h4><div class="social"><span></span><span></span><span></span></div></div>

<div class="abs copyright">COPYRIGHT © 2020 KELVORO NETLINK ALL RIGHTS RESERVED</div>
</body>
</html>
```